" Temos como propósito desenvolver pessoas e proporcionar saúde transformando vidas e sorrisos. Acreditamos que a educação muda pessoas e essas transformam o mundo. E que a manutenção da saúde bucal é fundamental para a saúde geral e o aumento da auto-estima do indivíduo. Nosso principal serviço são os cursos de ortodontia para dentistas já formados (pós-graduação e cursos livres de ortodontia). Temos alguns outros cursos também para dentistas em outras áreas. "

```html
<!DOCTYPE html>
<html lang="pt-BR">
<head>
<meta charset="UTF-8">
<title>Assinatura de Email — Lumen Orto</title>
<link href="https://fonts.googleapis.com/css2?family=Open+Sans:wght@400;600;700&display=swap" rel="stylesheet">
<style>
  :root{
    --navy:#2e4358;
    --wine:#7a1d3c;
    --ink:#2b3a4a;
    --muted:#55616d;
    --rule:#b9bfc6;
    --paper:#ffffff;
    --backdrop:#e6e6e6;
  }
  *{margin:0;padding:0;box-sizing:border-box}
  html,body{width:1200px;height:1200px;overflow:hidden;background:var(--backdrop);font-family:"Open Sans",Arial,sans-serif}
  .signature{position:absolute;left:50px;top:432px;width:1100px;height:335px;background:var(--paper)}
  .signature__art{position:absolute;inset:0}
  .brand{position:absolute;left:40px;top:118px;width:330px;text-align:center;color:#fff;font-weight:600;font-size:52px;letter-spacing:1px;line-height:1}
  .side-bar{position:absolute;right:0;top:22px;width:25px;height:313px;background:var(--navy)}
  .details{position:absolute;left:605px;top:48px;width:400px;color:var(--ink)}
  .details__name{font-size:24px;font-weight:400;line-height:1.2}
  .details__name strong{font-weight:700}
  .details__role{font-size:14px;color:var(--muted);margin-top:2px}
  .details__rule{height:1px;background:var(--rule);margin:16px 0 0;width:390px}
  .contact{list-style:none;margin-top:18px}
  .contact__item{display:flex;align-items:center;gap:14px;font-size:14px;line-height:1.15;color:var(--ink);margin-bottom:13px}
  .contact__icon{width:24px;height:24px;flex:0 0 24px;border-radius:50%;background:var(--navy);display:flex;align-items:center;justify-content:center}
  .contact__icon svg{width:13px;height:13px}
  .contact__rule{height:1px;background:var(--rule);width:390px;margin-top:6px}
</style>
</head>
<body>
  <section class="signature">
    <svg class="signature__art" viewBox="0 0 1100 335" width="1100" height="335">
      <path d="M0 0 H395 Q520 150 505 335 H0 Z" fill="var(--wine)" opacity="0.35"/>
      <path d="M0 0 H375 Q500 150 485 335 H0 Z" fill="var(--wine)"/>
      <path d="M0 0 H345 Q470 150 450 335 H0 Z" fill="var(--navy)" role="img" aria-label="Painel azul-marinho com textura de listras diagonais sutis"/>
    </svg>
    <div class="brand">Lumen Orto</div>
    <div class="side-bar"></div>

    <div class="details">
      <p class="details__name"><strong>Nome</strong> Sobrenome</p>
      <p class="details__role">Cargo - Função</p>
      <div class="details__rule"></div>
      <ul class="contact">
        <li class="contact__item">
          <span class="contact__icon"><svg viewBox="0 0 24 24"><path fill="#fff" d="M6.6 10.8a15.1 15.1 0 0 0 6.6 6.6l2.2-2.2a1 1 0 0 1 1-.25 11.4 11.4 0 0 0 3.6.57 1 1 0 0 1 1 1V20a1 1 0 0 1-1 1A17 17 0 0 1 3 4a1 1 0 0 1 1-1h3.5a1 1 0 0 1 1 1c0 1.25.2 2.45.57 3.57a1 1 0 0 1-.25 1z"/></svg></span>
          <span>11 9876-5432<br>11 9876-5432</span>
        </li>
        <li class="contact__item">
          <span class="contact__icon"><svg viewBox="0 0 24 24"><path fill="#fff" d="M3 5h18v14H3z"/><path fill="none" stroke="#2e4358" stroke-width="2" d="M3 6l9 7 9-7"/></svg></span>
          <span>email@email.com</span>
        </li>
        <li class="contact__item">
          <span class="contact__icon"><svg viewBox="0 0 24 24"><g fill="none" stroke="#fff" stroke-width="2.6" stroke-linecap="round"><path d="M10 14a4 4 0 0 0 5.7 0l3-3a4 4 0 0 0-5.7-5.7l-1 1"/><path d="M14 10a4 4 0 0 0-5.7 0l-3 3a4 4 0 0 0 5.7 5.7l1-1"/></g></svg></span>
          <span>www.site.com</span>
        </li>
        <li class="contact__item">
          <span class="contact__icon"><svg viewBox="0 0 24 24"><path fill="#fff" d="M12 2a7 7 0 0 0-7 7c0 5 7 13 7 13s7-8 7-13a7 7 0 0 0-7-7zm0 9.5A2.5 2.5 0 1 1 12 6.5a2.5 2.5 0 0 1 0 5z"/></svg></span>
          <span>Endereço Completo<br>Bairro - Cidade - Estado - Cep</span>
        </li>
      </ul>
      <div class="contact__rule"></div>
    </div>
  </section>
</body>
</html>
```